877 stay Bold

Redesigning this front and back business card flyer and keeping the info but making it look better.

This is all about using the info and logo on the business card design and creating a better layout using any of the following and more.

Changing the background color or imagine, chaining the placement of content, resizing content.

Target Market(s)

Targeting people that have been injured on one side and people that have been giving a DUI on the other.

Contact Information for Business Card

We are looking to keep the info but make it look a fee cleaner and less cluttered

Font styles to use
Sans Serif

Requirements
Must have
• Must have the same info but a better layout.
Nice to have
• better background colors or image or layout. different fonts or same font all design options that will make it look professional and clean.

```html
<!DOCTYPE html>
<html lang="en">
<head>
<meta charset="utf-8">
<title>877 Stay Bold – Injury &amp; DUI Cards</title>
<link href="https://fonts.googleapis.com/css2?family=Alfa+Slab+One&family=Montserrat:wght@600;700;800;900&display=swap" rel="stylesheet">
<style>
  :root{
    --red:#d81e35;
    --ink:#0d0506;
    --white:#ffffff;
    --bg:#f3f3f3;
    --photo-dark:#2c3f5c;
    --photo-mid:#5b7ba3;
    --photo-light:#9fb5cf;
  }
  *{box-sizing:border-box;margin:0;padding:0}
  html,body{width:1200px;height:1000px;overflow:hidden}
  body{background:var(--bg);font-family:"Montserrat",Arial,sans-serif;position:relative}
  .card{position:absolute;width:338px;height:564px;background:var(--white);overflow:hidden}
  .card--injury{left:188px;top:205px}
  .card--dui{left:666px;top:207px}
  .abs{position:absolute}
  .photo{position:absolute}

  /* injury card */
  .photo--crash{left:0;top:0;width:338px;height:167px;background:linear-gradient(160deg,var(--photo-light),var(--photo-mid) 45%,var(--photo-dark))}
  .photo--back{left:0;top:167px;width:169px;height:118px;background:linear-gradient(120deg,#1a2436,#4c6a93 60%,#2a3a55)}
  .photo--xray{left:169px;top:167px;width:169px;height:118px;background:linear-gradient(140deg,#1d2c46,#6f8db5 55%,#c4d3e4)}
  .brand-band{left:0;top:0;width:248px;height:57px}
  .brand{left:10px;top:8px;display:flex;align-items:center;gap:8px;color:var(--white);font-weight:800;font-size:30px;letter-spacing:.5px;line-height:40px}
  .brand-dot{width:14px;height:14px;border-radius:50%;background:var(--white)}
  .injured-banner{left:0;top:253px;width:338px;height:40px}
  .injured-text{left:44px;top:258px;color:var(--white);font-weight:700;font-size:20px}
  .headline-band{left:0;top:291px;width:338px;height:38px;background:var(--ink);color:var(--white);font-family:"Alfa Slab One",Georgia,serif;font-size:27px;text-align:center;line-height:40px;letter-spacing:.5px}
  .reasons{left:6px;top:342px;list-style:none}
  .reasons li{display:flex;align-items:center;gap:6px;height:26px;font-weight:900;font-size:14.5px;color:var(--ink);letter-spacing:-.1px}
  .reasons svg{flex:none}
  .cta{height:30px;border-radius:15px;background:var(--red);color:var(--white);font-weight:700;font-size:16.5px;text-align:center;line-height:30px}
  .card--injury .cta{left:63px;top:450px;width:210px}
  .url{color:var(--red);font-weight:700;font-size:16px;text-align:center;width:338px;left:0}
  .card--injury .url{top:482px}
  .footer{left:0;width:338px;background:var(--ink);color:var(--white);font-weight:700;text-align:center}
  .card--injury .footer{top:510px;height:54px;font-size:14px;line-height:20px;padding-top:7px}

  /* dui card */
  .dui-banner{left:0;top:0;width:338px;height:38px}
  .dui-slab{left:0;top:0;width:338px;height:38px;color:var(--white);font-family:"Alfa Slab One",Georgia,serif;font-size:27px;text-align:center;line-height:40px;padding-left:6px}
  .dui-sub{left:0;top:38px;width:338px;height:40px;background:var(--ink);color:var(--white);font-weight:700;font-size:24px;text-align:center;line-height:40px}
  .question{left:0;top:90px;width:338px;text-align:center;font-weight:800;font-size:18px;line-height:24px;color:var(--ink)}
  .question em{font-style:normal;color:var(--red)}
  .steps{left:16px;top:148px;width:318px;list-style:none}
  .steps li{position:relative;padding-left:33px;font-weight:700;font-size:14.5px;line-height:20px;color:var(--ink);margin-bottom:4px}
  .steps li svg{position:absolute;left:0;top:-3px}
  .steps strong{color:var(--red);font-weight:800}
  .rule{left:0;top:414px;width:338px;height:4px;background:var(--red)}
  .photo--driver{left:0;top:419px;width:170px;height:100px;background:linear-gradient(150deg,#b7c6d8,#6a84a6 50%,#2d3e58)}
  .photo--passenger{left:172px;top:419px;width:166px;height:100px;background:linear-gradient(150deg,#2a3b55,#5f7fa6 55%,#1b2639)}
  .card--dui .footer{top:519px;height:45px}
  .card--dui .cta{left:62px;top:501px;width:210px}
  .card--dui .url{top:534px;color:var(--white);font-size:16px}
</style>
</head>
<body>

<section class="card card--injury">
  <div class="photo photo--crash" role="img" aria-label="Photo of a cyclist sitting on the road beside a fallen bicycle after a collision with a car"></div>
  <div class="photo photo--back" role="img" aria-label="Photo of a person holding their lower back in pain"></div>
  <div class="photo photo--xray" role="img" aria-label="Photo of a doctor pointing at a hand X-ray"></div>

  <svg class="abs brand-band" viewBox="0 0 248 57" aria-hidden="true">
    <polygon points="0,0 248,0 222,57 0,57" fill="var(--ink)"/>
    <polygon points="0,0 240,0 214,53 0,53" fill="var(--red)"/>
  </svg>
  <div class="abs brand">877 STAY BOLD <span class="brand-dot"></span></div>

  <svg class="abs injured-banner" viewBox="0 0 338 40" aria-hidden="true">
    <polygon points="30,0 338,0 338,40 14,40" fill="var(--red)"/>
  </svg>
  <p class="abs injured-text">If you’ve been injured</p>
  <h2 class="abs headline-band">STAY BOLD</h2>

  <ul class="abs reasons">
    <li><svg width="42" height="20" viewBox="0 0 42 20"><polygon points="0,0 42,0 36,20 0,20" fill="var(--red)"/><path d="M16 5l9 10M25 5l-9 10" stroke="var(--white)" stroke-width="2.8" stroke-linecap="round"/></svg>For an inexperienced lawyer!</li>
    <li><svg width="42" height="20" viewBox="0 0 42 20"><polygon points="0,0 42,0 36,20 0,20" fill="var(--red)"/><path d="M16 5l9 10M25 5l-9 10" stroke="var(--white)" stroke-width="2.8" stroke-linecap="round"/></svg>For less than you deserve!</li>
    <li><svg width="42" height="20" viewBox="0 0 42 20"><polygon points="0,0 42,0 36,20 0,20" fill="var(--red)"/><path d="M16 5l9 10M25 5l-9 10" stroke="var(--white)" stroke-width="2.8" stroke-linecap="round"/></svg>For paying massive medical bills!</li>
    <li><svg width="42" height="20" viewBox="0 0 42 20"><polygon points="0,0 42,0 36,20 0,20" fill="var(--red)"/><path d="M16 5l9 10M25 5l-9 10" stroke="var(--white)" stroke-width="2.8" stroke-linecap="round"/></svg>For a life of pain and debt!</li>
  </ul>

  <div class="abs cta">CALL 877-555-0142</div>
  <p class="abs url">www.877StayBold.com</p>
  <p class="abs footer">WE FIGHT FOR YOU, SO YOU CAN<br>FOCUS ON GETTING BETTER</p>
</section>

<section class="card card--dui">
  <div class="abs dui-sub">FOR A DUI</div>
  <svg class="abs dui-banner" viewBox="0 0 338 38" aria-hidden="true">
    <rect width="338" height="38" fill="var(--ink)"/>
    <polygon points="30,0 338,0 338,38 14,38" fill="var(--red)"/>
  </svg>
  <h2 class="abs dui-slab">STAY BOLD</h2>

  <p class="abs question">WHAT SHOULD I DO IF<br>I GET PULLED OVER FOR <em>DUI</em>?</p>

  <ul class="abs steps">
    <li><svg width="30" height="26" viewBox="0 0 30 26"><path d="M2 14l8 8L28 2" fill="none" stroke="var(--red)" stroke-width="5" stroke-linejoin="round"/></svg>Pull over in a calm, normal manner</li>
    <li><svg width="30" height="26" viewBox="0 0 30 26"><path d="M2 14l8 8L28 2" fill="none" stroke="var(--red)" stroke-width="5" stroke-linejoin="round"/></svg>Be polite at all times</li>
    <li><svg width="30" height="26" viewBox="0 0 30 26"><path d="M2 14l8 8L28 2" fill="none" stroke="var(--red)" stroke-width="5" stroke-linejoin="round"/></svg><strong>DO NOT</strong> admit to drinking</li>
    <li><svg width="30" height="26" viewBox="0 0 30 26"><path d="M2 14l8 8L28 2" fill="none" stroke="var(--red)" stroke-width="5" stroke-linejoin="round"/></svg><strong>DO NOT</strong> submit to any held sobriety tests</li>
    <li><svg width="30" height="26" viewBox="0 0 30 26"><path d="M2 14l8 8L28 2" fill="none" stroke="var(--red)" stroke-width="5" stroke-linejoin="round"/></svg><strong>DO NOT</strong> submit to taking a chemical test (breath, blood or urine)</li>
    <li><svg width="30" height="26" viewBox="0 0 30 26"><path d="M2 14l8 8L28 2" fill="none" stroke="var(--red)" stroke-width="5" stroke-linejoin="round"/></svg><strong>DO NOT</strong> make any statement after being arrested, especially when placed in the police cruiser.</li>
  </ul>

  <div class="abs rule"></div>
  <div class="photo photo--driver" role="img" aria-label="Photo of a stressed man resting his head on the steering wheel"></div>
  <div class="photo photo--passenger" role="img" aria-label="Photo of a worried woman sitting in a car"></div>
  <div class="abs footer"></div>
  <div class="abs cta">CALL 877-555-0142</div>
  <p class="abs url">www.877StayBold.com</p>
</section>

</body>
</html>
```